Infographic for a Christian church discipleship pathway

We need to take a fairly complex program that helps people in a Baptist church follow Jesus, and turn it into a simple graphic. This graphic does not have to explain the whole program, web pages and print materials will do that. But, it should be something that people see and understand what it is quickly. The attached graphic is only to give the key words and general direction of the program. It should not serve as a design guide. In other words, we want to see some other ideas how this information can be imparted graphically with concision and creativity. It's important to note, the categories at the top (pray daily, read daily, gather weekly) are first steps, starting points....one shouldn't move forward until they've incorporated these things into their life. However, the categories that follow (study, connect, serve, etc) are not necessarily steps to take in sequential order.

The diagrams we've provided are not what we expect. They are only to explain the program. Here is a verbal description: The motto of our church is "A Ready Church" (ready to serve, ready to love, ready for when Jesus returns). There are four words that describe a ready church member: FOCUSED on the return of Christ, FAITHFUL in a daily relationship with Jesus, PREPARED for any opportunity to be a supernatural vessel of God's worK, LOOKING to invite others into God's family. The first two are God's Work in Me (Focused and faithful); the second two are God's Work Through me (Prepared, looking). Please use those two things as you wish (Focused faithful prepared looking; and God's word in and through me). If they are clarifying, please use. If not, you don't have to use.

Additionally, the strategies we employ to be "a ready church" are 1. Prayer 2. God's Word, and 3. Biblical Community. (So, in other words, these three things help us be a people who is focused, faithful, prepared, and looking....which is a ready church.

To provide some information how we will build this out: this graphic will be used in print and digital content. The digital content will allow people to click on each category to access training and resources associated with that discipline. (Fasting, reflecting, etc).

www.kwm.parish

Target Market(s)

35-50

Industry/Entity Type

Religious

Other font styles liked:
• Lato and/or Cambria

Requirements
Must have
• Fonts: lato, cambria. Colors#: 373E41, ebebe8, #a69677. Accent Colors: 80401D, #4e5730, #a5bac8
Nice to have
• A designer who has an understanding of what it means to incorporate the spiritual disciplines of the Christian faith into their life.

```html
<!DOCTYPE html>
<html lang="en">
<head>
<meta charset="utf-8">
<title>Three Steps to Ready Life</title>
<link href="https://fonts.googleapis.com/css2?family=Caladea:wght@400;700&family=Lato:wght@400;900&display=swap" rel="stylesheet">
<style>
  :root {
    --ink: #000000;
    --paper: #ffffff;
    --gold: #a69677;
    --pray-rest: #8a9ca6;
    --pray-fast: #b7cadb;
    --word-study: #80562e;
    --word-teach: #cca582;
    --gather-connect: #4a672e;
    --gather-give: #98ac3a;
    --in-you: #4e6a2e;
    --through-you: #98ac3a;
  }
  * { margin: 0; padding: 0; box-sizing: border-box; }
  html, body { width: 1200px; height: 818px; overflow: hidden; background: var(--paper); }
  .canvas { position: relative; width: 1200px; height: 818px; font-family: "Caladea", Cambria, serif; color: var(--ink); }

  .brand-mark { position: absolute; left: 558px; top: 94px; width: 90px; height: 104px; border: 3px solid var(--gold); }

  .title { position: absolute; left: 18px; width: 1200px; top: 222px; text-align: center; font-weight: 700; font-size: 43px; letter-spacing: 0.5px; color: var(--gold); }

  .tile { position: absolute; height: 98px; padding: 0 13px; display: flex; align-items: center; justify-content: space-between; }
  .tile-words { font-size: 22px; line-height: 25px; letter-spacing: 0.5px; }
  .tile-in .tile-words { text-align: right; }
  .tile-icon { width: 68px; height: 68px; flex: none; }
  .tile-icon svg { width: 100%; height: 100%; fill: none; stroke: var(--paper); stroke-width: 2.6; stroke-linecap: round; stroke-linejoin: round; }

  .rest { left: 340px; width: 195px; top: 313px; background: var(--pray-rest); }
  .fast { left: 663px; width: 195px; top: 313px; background: var(--pray-fast); }
  .study { left: 230px; width: 305px; top: 432px; background: var(--word-study); }
  .teach { left: 663px; width: 305px; top: 432px; background: var(--word-teach); }
  .connect { left: 109px; width: 426px; top: 551px; background: var(--gather-connect); }
  .give { left: 663px; width: 426px; top: 551px; background: var(--gather-give); }

  .step { position: absolute; left: 531px; width: 140px; text-align: center; }
  .step-number { display: block; width: 70px; height: 70px; margin: 0 auto; border-radius: 50%; background: var(--ink); color: var(--paper); font-family: "Lato", sans-serif; font-weight: 900; font-size: 58px; line-height: 70px; }
  .step-label { display: block; margin-top: 12px; font-weight: 700; font-size: 16.5px; white-space: nowrap; }
  .step-pray { top: 310px; }
  .step-read { top: 431px; }
  .step-gather { top: 551px; }

  .brackets { position: absolute; left: 0; top: 0; width: 1200px; height: 818px; }
  .brackets path { fill: none; stroke-width: 11; }
  .bracket-in { stroke: var(--in-you); }
  .bracket-through { stroke: var(--through-you); }

  .note { position: absolute; text-align: center; font-weight: 700; font-size: 13.5px; line-height: 16px; letter-spacing: 0.3px; white-space: nowrap; }
  .note-in { left: 220px; width: 180px; top: 678px; color: var(--in-you); }
  .note-center { left: 521px; width: 160px; top: 668px; color: var(--ink); }
  .note-through { left: 781px; width: 180px; top: 668px; color: var(--through-you); }
</style>
</head>
<body>
<main class="canvas">
  <span class="brand-mark" aria-hidden="true"></span>

  <h1 class="title">THREE STEPS TO READY LIFE</h1>

  <!-- Step 1: prayer -->
  <section class="tile tile-in rest">
    <span class="tile-icon"><svg viewBox="0 0 66 66"><path d="M14 14c4-4 9 0 12 6l9 16V22c0-4 4-5 6-2v24l9 12"/><path d="M9 22l13 22 10 12"/><path d="M12 17l12 20"/><path d="M18 13l11 19"/></svg></span>
    <p class="tile-words">REST<br>REFLECT</p>
  </section>
  <div class="step step-pray"><span class="step-number">1</span><span class="step-label">PRAY DAILY</span></div>
  <section class="tile tile-through fast">
    <p class="tile-words">FAST<br>INTERCEDE</p>
    <span class="tile-icon"><svg viewBox="0 0 66 66"><path d="M52 14c-4-4-9 0-12 6l-9 16V22c0-4-4-5-6-2v24l-9 12"/><path d="M57 22L44 44 34 56"/><path d="M54 17L42 37"/><path d="M48 13L37 32"/></svg></span>
  </section>

  <!-- Step 2: God's word -->
  <section class="tile tile-in study">
    <span class="tile-icon"><svg viewBox="0 0 66 66"><path d="M6 20l2 32c10 0 18 2 25 5 7-3 15-5 25-5l2-32"/><path d="M12 16c9 0 16 2 21 7 5-5 12-7 21-7"/><path d="M16 10c7 1 12 3 17 8 5-5 10-7 17-8"/><path d="M31 26v26M35 26v26"/></svg></span>
    <p class="tile-words">STUDY<br>MEMORIZE</p>
  </section>
  <div class="step step-read"><span class="step-number">2</span><span class="step-label">READ DAILY</span></div>
  <section class="tile tile-through teach">
    <p class="tile-words">TEACH<br>PROCLAIM</p>
    <span class="tile-icon"><svg viewBox="0 0 66 66"><path d="M6 20l2 32c10 0 18 2 25 5 7-3 15-5 25-5l2-32"/><path d="M12 16c9 0 16 2 21 7 5-5 12-7 21-7"/><path d="M16 10c7 1 12 3 17 8 5-5 10-7 17-8"/><path d="M31 26v26M35 26v26"/></svg></span>
  </section>

  <!-- Step 3: biblical community -->
  <section class="tile tile-in connect">
    <span class="tile-icon"><svg viewBox="0 0 66 66"><circle cx="33" cy="10" r="7"/><path d="M24 26c3-4 6-4 9 0 3-4 6-4 9 0"/><circle cx="15" cy="32" r="7"/><circle cx="51" cy="32" r="7"/><path d="M3 62V48c4-5 8-5 12 0 4-5 8-5 12 0v14"/><path d="M39 62V48c4-5 8-5 12 0 4-5 8-5 12 0v14"/></svg></span>
    <p class="tile-words">CONNECT<br>LEARN</p>
  </section>
  <div class="step step-gather"><span class="step-number">3</span><span class="step-label">GATHER DAILY</span></div>
  <section class="tile tile-through give">
    <p class="tile-words">GIVE<br>SERVE</p>
    <span class="tile-icon"><svg viewBox="0 0 66 66"><circle cx="33" cy="10" r="7"/><path d="M24 26c3-4 6-4 9 0 3-4 6-4 9 0"/><circle cx="15" cy="32" r="7"/><circle cx="51" cy="32" r="7"/><path d="M3 62V48c4-5 8-5 12 0 4-5 8-5 12 0v14"/><path d="M39 62V48c4-5 8-5 12 0 4-5 8-5 12 0v14"/></svg></span>
  </section>

  <svg class="brackets" viewBox="0 0 1200 818" aria-hidden="true">
    <path class="bracket-in" d="M114 684V693Q114 701 122 701H232M392 701H522Q530 701 530 693V684"/>
    <path class="bracket-through" d="M675 684V693Q675 701 683 701H792M951 701H1083Q1091 701 1091 693V684"/>
  </svg>

  <p class="note note-in">GOD’S WORK IN YOU<br>AWAKENS FOCUS<br>AND&nbsp; FAITHFULNESS</p>
  <p class="note note-center">ESTABLISHES THE<br>RHYTHMS OF A<br>READY LIFE WITH<br>COMMUNITY, PRAYER<br>AND GOD’S WORD</p>
  <p class="note note-through">GOD’S WORK<br>THROUGH YOU KEEPS<br>YOU PREPARED<br>AND LOOKING</p>
</main>
</body>
</html>
```